Redesign the CTA buttons and scheenshots

https://www.plomvra.com/design/kT7wPqz2LmX9nBv4HsYcRe/04122024-Basketlyn-Final-v5?node-id=46-40225&t=ab3xk9Lm2QpVwZr7-1
Basketlyn is a collaborative shopping app that brings everything into one place.
Users can shop with friends and family and make product decisions together instead of shopping alone.

I’m redesigning the app’s action buttons (CTAs) and the App Store screenshots to improve clarity, engagement, and conversion. I’ve provided example App Store pages and competitor links for reference.

In Figma, I’ve highlighted the specific buttons and areas that need attention, along with clear instructions and context for each change.

If you see opportunities to improve any app buttons or strengthen the call-to-action, please review those areas and submit your suggested improvements.

Industry/Entity Type

Social Shopping

Number of Pages Required

1 page

Font styles to use
Other font styles liked:
• Use our Color Legend

Requirements
Must have
• Screenshots for the app store and New users and signed up users

```html
<!DOCTYPE html>
<html lang="en">
<head>
<meta charset="utf-8">
<title>Basketlyn – App Screens</title>
<link href="https://fonts.googleapis.com/css2?family=Rubik:wght@400;500;600&display=swap" rel="stylesheet">
<style>
:root{
  --bg:#575757;
  --white:#ffffff;
  --surface:#f6f5f7;
  --ink:#1d1d22;
  --muted:#6b6b73;
  --tile-text:#555555;
  --purple:#8c1fb2;
  --pink:#e83a88;
  --grad:linear-gradient(90deg,#8a1fb4 0%,#e33f8e 100%);
  --soft:#f6e3f4;
  --line:#d8d8dc;
  --green:#36c23b;
  --amber:#f3a61b;
}
*{box-sizing:border-box;margin:0;padding:0}
html,body{width:1082px;height:1200px;overflow:hidden;background:var(--bg)}
body{font-family:'Rubik',sans-serif;color:var(--ink)}
h1,h2,p{font-weight:400}
.stage{position:absolute;left:0;top:0;width:1536px;height:1704px;transform:scale(.70443);transform-origin:0 0}
.screen{position:absolute;width:414px;background:var(--surface);border-radius:40px;overflow:hidden}
.screen>*{position:absolute}
.topbar{left:0;top:0;width:414px;height:92px;background:var(--white);box-shadow:0 4px 14px rgba(0,0,0,.04)}
.round-btn{width:36px;height:36px;border-radius:50%;background:var(--grad);display:flex;align-items:center;justify-content:center;top:28px}
.round-btn.back{left:33px}.round-btn.menu{left:345px}
.title{left:0;width:414px;text-align:center;font-size:17px;font-weight:400;letter-spacing:.5px;color:var(--ink)}
.handle{font-size:14px;color:var(--muted)}
.section-h{left:32px;font-size:18px;font-weight:500;letter-spacing:.4px}
.link{right:34px;font-size:13px;color:var(--purple);text-decoration:underline}
.dashed{left:32px;width:350px;border-top:1.5px dashed #b9b9c0}
.dashed.pinkish{border-color:#d276d7}
.cta{display:flex;align-items:center;gap:12px;background:var(--grad);color:#fff;border-radius:24px;font-size:16px;padding-left:9px;box-shadow:0 6px 14px rgba(200,40,150,.25)}
.cta .dot{width:28px;height:28px;border-radius:50%;background:#fff;display:flex;align-items:center;justify-content:center}
.photo{border-radius:22px}
.pill{display:flex;align-items:center;gap:10px;height:46px;border-radius:23px;background:#fbeefa;border:1px solid #ecd0ec;padding-left:8px;font-size:15px;color:#444}
.pill .ic{width:30px;height:30px;border-radius:50%;background:var(--grad)}
.member{left:34px;width:346px;height:64px;background:#fff;border-radius:32px;box-shadow:0 4px 12px rgba(0,0,0,.05)}
.member .av{position:absolute;left:12px;top:8px;width:48px;height:48px;border-radius:50%;background:linear-gradient(135deg,#8a6a55,#3d4a52)}
.member .name{position:absolute;left:77px;top:15px;font-size:14px;font-weight:500}
.member .status{position:absolute;left:77px;top:35px;font-size:12.5px;color:#555;display:flex;align-items:center;gap:7px}
.member .status i{width:8px;height:8px;border-radius:50%;background:var(--green)}
.member .status i.away{background:var(--amber)}
.member .go{position:absolute;right:16px;top:16px;width:32px;height:32px;border-radius:50%;background:#f1f1f3;display:flex;align-items:center;justify-content:center}
.badge{width:20px;height:20px;border-radius:50%;background:var(--grad);display:flex;align-items:center;justify-content:center}
.stars{font-size:11px;color:#f2a612;letter-spacing:1px}
.pname{font-size:14px;color:#555;line-height:21px}
.price{font-size:18px;font-weight:600}
.meta{font-size:12.5px;color:#666;display:flex;align-items:center;gap:6px}
.meta b{color:var(--purple);font-weight:400}
.soft-btn{height:35px;border-radius:18px;background:var(--soft);color:var(--purple);font-size:14px;display:flex;align-items:center;justify-content:center}
.solid-btn{height:36px;border-radius:18px;background:var(--purple);color:#fff;font-size:15px;font-weight:500;display:flex;align-items:center;justify-content:center}
.scroll{left:32px;width:382px;height:2px;background:#d5d5d9}
.scroll::before{content:"";position:absolute;left:0;top:-1px;width:62px;height:4px;border-radius:2px;background:#444}
.nav{left:48px;width:318px;height:58px;border-radius:29px;background:var(--grad);display:flex;align-items:center;padding:0 8px;gap:12px;box-shadow:0 8px 18px rgba(190,40,150,.3)}
.nav .it{width:44px;height:44px;border-radius:50%;background:rgba(255,255,255,.2);display:flex;align-items:center;justify-content:center}
.nav .on{height:44px;border-radius:22px;background:rgba(255,255,255,.22);display:flex;align-items:center;gap:12px;padding:0 16px 0 6px;color:#fff;font-size:16px}
.nav .on .it{background:#fff;width:34px;height:34px}
.center-h{left:0;width:414px;text-align:center;font-size:16px;font-weight:500;line-height:26px;letter-spacing:.3px}
.para{left:40px;width:334px;text-align:center;font-size:14.5px;line-height:24px;color:#555}
.para b{color:var(--purple);font-weight:400}
.tile{width:82px;height:88px;background:#fff;border-radius:8px;border:1px solid #f1dcec;display:flex;flex-direction:column;align-items:center;padding-top:16px;gap:10px;font-size:14px;color:var(--tile-text)}
.tile .lbl{color:var(--tile-text);font-size:14px}
.tile .mk{width:30px;height:30px;border-radius:50%;background:#fff;box-shadow:0 2px 6px rgba(0,0,0,.12);display:flex;align-items:center;justify-content:center}
.tile .mk i{width:12px;height:12px;border-radius:50%;background:var(--c,#222)}
.heart{position:absolute;right:8px;top:8px}
.sorter{width:61px;height:34px;border-radius:17px;background:var(--purple);color:#fff;font-size:12px;display:flex;align-items:center;justify-content:center;gap:10px}
.search{left:34px;width:346px;height:46px;border-radius:23px;background:var(--grad);color:#fff;font-size:16px;display:flex;align-items:center;gap:12px;padding-left:8px}
.search .dot{width:30px;height:30px;border-radius:50%;background:#fff;display:flex;align-items:center;justify-content:center}
.card-img{width:165px;height:180px;border-radius:18px}
.card-img .bm{position:absolute;right:10px;top:14px;width:22px;height:22px;border-radius:50%;background:var(--grad);display:flex;align-items:center;justify-content:center}
.ctitle{font-size:14px;color:#555;line-height:21px;width:165px}
.count{display:flex;align-items:center;gap:12px}
.avs{display:flex}
.avs i{width:26px;height:26px;border-radius:50%;border:2px solid #fff;margin-left:-8px;background:linear-gradient(135deg,#e7904a,#5a87b8)}
.avs i:first-child{margin-left:0}
.num{font-size:17px;font-weight:600;line-height:18px}
.num span{display:block;font-size:14px;font-weight:400;color:#555}
</style>
</head>
<body>
<svg width="0" height="0" style="position:absolute">
  <defs>
    <symbol id="chev" viewBox="0 0 24 24"><path d="M14 6l-6 6 6 6" fill="none" stroke="#fff" stroke-width="2.6" stroke-linecap="round" stroke-linejoin="round"/></symbol>
    <symbol id="grid" viewBox="0 0 24 24"><rect x="5" y="5" width="6" height="6" rx="1.5" fill="#fff"/><rect x="13" y="5" width="6" height="6" rx="1.5" fill="#fff"/><rect x="5" y="13" width="6" height="6" rx="1.5" fill="#fff"/><rect x="13" y="13" width="6" height="6" rx="1.5" fill="#fff"/></symbol>
    <symbol id="arrow" viewBox="0 0 24 24"><path d="M5 12h13M13 7l5 5-5 5" fill="none" stroke="#333" stroke-width="1.6" stroke-linecap="round" stroke-linejoin="round"/></symbol>
    <symbol id="home" viewBox="0 0 24 24"><path d="M4 11l8-7 8 7v9h-5v-6h-6v6H4z" fill="#fff"/></symbol>
    <symbol id="home-pink" viewBox="0 0 24 24"><path d="M4 11l8-7 8 7v9h-5v-6h-6v6H4z" fill="#c02d9a"/></symbol>
    <symbol id="store" viewBox="0 0 24 24"><path d="M4 5h16l1 5H3zM5 11h14v9H5z" fill="#fff"/><rect x="10" y="14" width="4" height="6" fill="#d0409a"/></symbol>
    <symbol id="store-pink" viewBox="0 0 24 24"><path d="M4 5h16l1 5H3zM5 11h14v9H5z" fill="#c02d9a"/><rect x="10" y="14" width="4" height="6" fill="#fff"/></symbol>
    <symbol id="play-pink" viewBox="0 0 24 24"><path d="M8 5l11 7-11 7z" fill="#c02d9a"/></symbol>
    <symbol id="globe" viewBox="0 0 24 24"><circle cx="12" cy="12" r="8" fill="none" stroke="#fff" stroke-width="1.8"/><path d="M4 12h16M12 4c3 3 3 13 0 16M12 4c-3 3-3 13 0 16" fill="none" stroke="#fff" stroke-width="1.6"/></symbol>
    <symbol id="chat" viewBox="0 0 24 24"><path d="M4 12a8 7 0 1 1 4 6l-4 2 1-4a7 7 0 0 1-1-4z" fill="#fff"/></symbol>
    <symbol id="plus" viewBox="0 0 24 24"><circle cx="12" cy="12" r="8" fill="#c02d9a"/><path d="M12 8v8M8 12h8" stroke="#fff" stroke-width="2"/></symbol>
    <symbol id="mag" viewBox="0 0 24 24"><circle cx="11" cy="11" r="5" fill="none" stroke="#c02d9a" stroke-width="2"/><path d="M15 15l4 4" stroke="#c02d9a" stroke-width="2" stroke-linecap="round"/></symbol>
    <symbol id="mark" viewBox="0 0 24 24"><path d="M7 4h10v16l-5-4-5 4z" fill="#fff"/></symbol>
    <symbol id="hrt" viewBox="0 0 24 24"><path d="M12 20S3 14 3 8.5A4.5 4.5 0 0 1 12 6a4.5 4.5 0 0 1 9 2.5C21 14 12 20 12 20z" fill="#e4191f"/></symbol>
    <symbol id="thumb" viewBox="0 0 24 24"><path d="M3 10h4v10H3zM9 10l4-7c2 0 2 2 2 3l-1 4h6l-2 10H9z" fill="#8c1fb2"/></symbol>
    <symbol id="thumbd" viewBox="0 0 24 24"><path d="M3 4h4v10H3zM9 4h9l2 10h-6l1 4c0 1 0 3-2 3l-4-7z" fill="none" stroke="#555" stroke-width="1.8"/></symbol>
    <symbol id="bubble" viewBox="0 0 24 24"><path d="M4 11a8 6 0 1 1 4 5l-4 2 1-3a6 6 0 0 1-1-4z" fill="none" stroke="#555" stroke-width="1.8"/></symbol>
  </defs>
</svg>

<main class="stage">

  <!-- HOME / EVENT SCREEN -->
  <section class="screen" style="left:90px;top:85px;height:1535px">
    <header class="topbar"></header>
    <div class="round-btn back"><svg width="20" height="20"><use href="#chev"/></svg></div>
    <div class="round-btn menu"><svg width="22" height="22"><use href="#grid"/></svg></div>
    <h1 class="title" style="top:23px">MARCUS'S 30TH BIRTHDAY</h1>
    <p class="title handle" style="top:48px">@marcusb</p>

    <div class="photo" role="img" aria-label="Birthday cake with lit candles and colourful balloons" style="left:57px;top:128px;width:300px;height:180px;background:radial-gradient(circle at 50% 60%,#f5d9a8 0%,#e7a063 30%,#c15a8e 60%,#4a7fc0 100%);border:3px solid #fff;box-shadow:0 6px 16px rgba(0,0,0,.12)"></div>

    <div class="pill" style="left:34px;top:343px;width:96px"><span class="ic"></span>Chat</div>
    <div class="pill" style="left:138px;top:343px;width:106px"><span class="ic"></span>Invite</div>
    <div class="pill" style="left:254px;top:343px;width:127px"><span class="ic"></span>Event Info</div>

    <p class="center-h" style="top:402px">TURN CONVERSATION INTO DECISIONS</p>
    <div class="cta" style="left:118px;top:437px;width:180px;height:46px"><span class="dot"><svg width="20" height="20"><use href="#plus"/></svg></span>Add To Wishlist</div>

    <div class="dashed" style="top:514px"></div>
    <h2 class="section-h" style="top:541px">MEMBERS (12)</h2>
    <a class="link" style="top:545px">View All</a>

    <div class="member" style="top:582px"><span class="av" role="img" aria-label="Member profile photo"></span><span class="name">EMMA</span><span class="status"><i></i>Active Now</span><span class="go"><svg width="18" height="18"><use href="#arrow"/></svg></span></div>
    <div class="member" style="top:664px"><span class="av" role="img" aria-label="Member profile photo"></span><span class="name">THOMPSON</span><span class="status"><i></i>Active Now</span><span class="go"><svg width="18" height="18"><use href="#arrow"/></svg></span></div>
    <div class="member" style="top:746px"><span class="av" role="img" aria-label="Member profile photo"></span><span class="name">NOAH</span><span class="status"><i class="away"></i>Last Seen 07:58</span><span class="go"><svg width="18" height="18"><use href="#arrow"/></svg></span></div>
    <div class="member" style="top:828px"><span class="av" role="img" aria-label="Member profile photo"></span><span class="name">SOPHIA</span><span class="status"><i></i>Active Now</span><span class="go"><svg width="18" height="18"><use href="#arrow"/></svg></span></div>

    <div class="dashed" style="top:934px"></div>
    <h2 class="section-h" style="top:961px">WISHLIST ITEMS (18)</h2>
    <a class="link" style="top:965px">Filter</a>

    <div class="photo" role="img" aria-label="White high-top sneaker product photo" style="left:33px;top:1008px;width:165px;height:180px;background:linear-gradient(160deg,#cfd8d4,#8fa79c 60%,#2f5b45)"><span class="badge" style="position:absolute;right:12px;top:14px"><svg width="12" height="12"><use href="#grid"/></svg></span></div>
    <div class="photo" role="img" aria-label="Black, white and red high-top sneaker product photo" style="left:216px;top:1008px;width:165px;height:180px;background:linear-gradient(160deg,#2a2a2a,#111 60%,#3a1414)"><span class="badge" style="position:absolute;right:12px;top:14px"><svg width="12" height="12"><use href="#grid"/></svg></span></div>

    <div style="left:33px;top:1206px;width:165px">
      <p class="stars">★★★★☆</p>
      <p class="pname" style="margin-top:6px">Swiftra High Top Mens Fashion Shoe</p>
      <p class="price" style="margin-top:4px">$109.90</p>
      <div style="border-top:1px solid var(--line);margin-top:8px;padding-top:10px" class="meta"><svg width="14" height="14"><use href="#thumb"/></svg><b>(04)</b> | <svg width="14" height="14"><use href="#thumbd"/></svg>(00)<svg width="14" height="14" style="margin-left:auto"><use href="#bubble"/></svg></div>
      <div class="soft-btn" style="margin-top:12px">Shopmarto.com</div>
    </div>
    <div style="left:216px;top:1206px;width:165px">
      <p class="stars">★★★★☆</p>
      <p class="pname" style="margin-top:6px">Swiftra High Top Mens Fashion Shoe</p>
      <p class="price" style="margin-top:4px">$109.90</p>
      <div style="border-top:1px solid var(--line);margin-top:8px;padding-top:10px" class="meta"><svg width="14" height="14"><use href="#thumb"/></svg><b>(04)</b> | <svg width="14" height="14"><use href="#thumbd"/></svg>(00)<svg width="14" height="14" style="margin-left:auto"><use href="#bubble"/></svg></div>
      <div class="soft-btn" style="margin-top:12px">Shopmarto.com</div>
    </div>

    <div class="scroll" style="top:1411px"></div>
    <nav class="nav" style="top:1449px">
      <span class="on"><span class="it"><svg width="20" height="20"><use href="#home-pink"/></svg></span>HOME</span>
      <span class="it"><svg width="22" height="22"><use href="#store"/></svg></span>
      <span class="it"><svg width="22" height="22"><use href="#globe"/></svg></span>
      <span class="it"><svg width="22" height="22"><use href="#chat"/></svg></span>
    </nav>
  </section>

  <!-- STORES SCREEN -->
  <section class="screen" style="left:561px;top:85px;height:1540px">
    <header class="topbar"></header>
    <div class="round-btn back"><svg width="20" height="20"><use href="#chev"/></svg></div>
    <div class="round-btn menu"><svg width="22" height="22"><use href="#grid"/></svg></div>
    <h1 class="title" style="top:36px">STORES</h1>

    <p class="center-h" style="top:120px">FIND YOUR FAVORITE ITEMS FROM<br>OUR RETAIL PARTNERS!</p>
    <p class="para" style="top:183px">Find products from any retailer, add them to your WishList with the <b>share</b>, and share it with friends and family.</p>
    <p class="para" style="top:279px;color:#333">Start your shared WishList now!</p>
    <div class="cta" style="left:112px;top:321px;width:190px;height:46px"><span class="dot"><svg width="16" height="16"><use href="#play-pink"/></svg></span>Watch the Demo</div>

    <div class="dashed" style="top:404px"></div>
    <h2 class="section-h" style="top:432px">FAVOURITES</h2>
    <a class="link" style="top:435px">View All</a>

    <div class="tile" style="left:33px;top:475px;--c:#7a6cf0"><span class="mk"><i></i></span><span class="lbl">Pickora</span></div>
    <div class="tile" style="left:122px;top:475px"><span class="mk"><i></i></span><span class="lbl">Treadmor</span></div>
    <div class="tile" style="left:211px;top:475px;--c:#1b2f8c"><span class="mk"><i></i></span><span class="lbl">Kinetra</span></div>
    <div class="tile" style="left:300px;top:475px"><span class="mk"><i></i></span><span class="lbl">Lowtop</span></div>

    <div class="tile" style="left:33px;top:580px;--c:#f2b400"><span class="mk"><i></i></span><span class="lbl">Workline</span></div>
    <div class="tile" style="left:122px;top:580px;--c:#1a73c9"><span class="mk"><i></i></span><span class="lbl">Ridgeway</span></div>
    <div class="tile" style="left:211px;top:580px;--c:#e22020"><span class="mk"><i></i></span><span class="lbl">Pouncer</span></div>
    <div class="tile" style="left:300px;top:580px"><span class="mk"><i></i></span><span class="lbl">Oakfield</span></div>

    <div class="tile" style="left:33px;top:686px;--c:#7a6cf0"><span class="mk"><i></i></span><span class="lbl">Pickora</span></div>
    <div class="tile" style="left:122px;top:686px"><span class="mk"><i></i></span><span class="lbl">Treadmor</span></div>
    <div class="tile" style="left:211px;top:686px;--c:#1b2f8c"><span class="mk"><i></i></span><span class="lbl">Kinetra</span></div>
    <div class="tile" style="left:300px;top:686px"><span class="mk"><i></i></span><span class="lbl">Lowtop</span></div>

    <div class="tile" style="left:33px;top:791px;--c:#f2b400"><span class="mk"><i></i></span><span class="lbl">Workline</span></div>
    <div class="tile" style="left:122px;top:791px;--c:#1a73c9"><span class="mk"><i></i></span><span class="lbl">Ridgeway</span></div>
    <div class="tile" style="left:211px;top:791px;--c:#e22020"><span class="mk"><i></i></span><span class="lbl">Pouncer</span></div>
    <div class="tile" style="left:300px;top:791px"><span class="mk"><i></i></span><span class="lbl">Oakfield</span></div>

    <div class="tile" style="left:33px;top:896px;--c:#7a6cf0"><span class="mk"><i></i></span><span class="lbl">Pickora</span></div>
    <div class="tile" style="left:122px;top:896px"><span class="mk"><i></i></span><span class="lbl">Treadmor</span></div>
    <div class="tile" style="left:211px;top:896px;--c:#1b2f8c"><span class="mk"><i></i></span><span class="lbl">Kinetra</span></div>
    <div class="tile" style="left:300px;top:896px"><span class="mk"><i></i></span><span class="lbl">Lowtop</span></div>

    <div class="dashed pinkish" style="top:1023px"></div>
    <h2 class="section-h" style="top:1049px">A</h2>
    <div class="sorter" style="left:319px;top:1043px">A <span>⇕</span></div>

    <div class="tile" style="left:33px;top:1094px"><span class="mk"><i></i></span><span class="lbl">Treadmor</span></div>
    <div class="tile" style="left:122px;top:1094px"><svg class="heart" width="12" height="12"><use href="#hrt"/></svg><span class="mk"><i></i></span><span class="lbl">Treadmor</span></div>
    <div class="tile" style="left:211px;top:1094px;--c:#1b2f8c"><svg class="heart" width="12" height="12"><use href="#hrt"/></svg><span class="mk"><i></i></span><span class="lbl">Kinetra</span></div>
    <div class="tile" style="left:300px;top:1094px"><span class="mk"><i></i></span><span class="lbl">Ummy</span></div>

    <div class="tile" style="left:33px;top:1199px"><span class="mk"><i></i></span><span class="lbl">Ummy</span></div>
    <div class="tile" style="left:122px;top:1199px"><svg class="heart" width="12" height="12"><use href="#hrt"/></svg><span class="mk"><i></i></span><span class="lbl">Ummy</span></div>
    <div class="tile" style="left:211px;top:1199px"><span class="mk"><i></i></span><span class="lbl">Ummy</span></div>
    <div class="tile" style="left:300px;top:1199px"><svg class="heart" width="12" height="12"><use href="#hrt"/></svg><span class="mk"><i></i></span><span class="lbl">Ummy</span></div>

    <div class="tile" style="left:33px;top:1303px"><span class="mk"><i></i></span><span class="lbl">Ummy</span></div>
    <div class="tile" style="left:122px;top:1303px"><svg class="heart" width="12" height="12"><use href="#hrt"/></svg><span class="mk"><i></i></span><span class="lbl">Ummy</span></div>
    <div class="tile" style="left:211px;top:1303px"><span class="mk"><i></i></span><span class="lbl">Ummy</span></div>
    <div class="tile" style="left:300px;top:1303px"><svg class="heart" width="12" height="12"><use href="#hrt"/></svg><span class="mk"><i></i></span><span class="lbl">Ummy</span></div>

    <div class="scroll" style="top:1422px"></div>
    <nav class="nav" style="top:1462px">
      <span class="it"><svg width="22" height="22"><use href="#home"/></svg></span>
      <span class="on"><span class="it"><svg width="20" height="20"><use href="#store-pink"/></svg></span>STORES</span>
      <span class="it"><svg width="22" height="22"><use href="#globe"/></svg></span>
      <span class="it"><svg width="22" height="22"><use href="#chat"/></svg></span>
    </nav>
  </section>

  <!-- DISCOVER SCREEN -->
  <section class="screen" style="left:1032px;top:85px;height:1211px">
    <header class="topbar"></header>
    <div class="round-btn back"><svg width="20" height="20"><use href="#chev"/></svg></div>
    <div class="round-btn menu"><svg width="22" height="22"><use href="#grid"/></svg></div>
    <h1 class="title" style="top:36px">DISCOVER</h1>

    <div class="search" style="top:127px"><span class="dot"><svg width="18" height="18"><use href="#mag"/></svg></span>Search for a Wishlist</div>

    <h2 class="section-h" style="top:205px">AUTOMOTIVE (61)</h2>
    <a class="link" style="top:208px">View All</a>

    <div class="card-img" role="img" aria-label="Mechanic fitting a brake disc in a workshop" style="left:34px;top:251px;background:linear-gradient(150deg,#3a3634,#8a6e55 55%,#e6a35a)"><span class="bm"><svg width="12" height="12"><use href="#mark"/></svg></span></div>
    <div class="card-img" role="img" aria-label="Red SUV driving on a blue lit road" style="left:218px;top:251px;background:linear-gradient(170deg,#9fc4d8,#3f6f8e 50%,#c23a2a 80%,#2a4a60)"><span class="bm"><svg width="12" height="12"><use href="#mark"/></svg></span></div>

    <p class="ctitle" style="left:34px;top:448px">Universal Car Parts for ANY Vehicle</p>
    <p class="ctitle" style="left:218px;top:448px">Top Rated<br>Car Accessories</p>
    <div class="count" style="left:34px;top:497px"><span class="avs"><i></i><i></i><i></i></span><p class="num">93<span>Members</span></p></div>
    <div class="count" style="left:218px;top:497px"><span class="avs"><i></i><i></i><i></i></span><p class="num">71<span>Members</span></p></div>
    <div class="soft-btn" style="left:34px;top:547px;width:165px">Invite</div>
    <div class="solid-btn" style="left:218px;top:547px;width:165px">Join</div>

    <div class="scroll" style="top:612px"></div>
    <div class="dashed pinkish" style="top:655px"></div>

    <h2 class="section-h" style="top:681px">BEAUTY &amp; HEALTH (56)</h2>
    <a class="link" style="top:684px">View All</a>

    <div class="card-img" role="img" aria-label="Stylist treating a client's hair in a salon" style="left:34px;top:727px;background:linear-gradient(150deg,#e9e6e2,#9a8170 50%,#3a2f2a)"><span class="bm"><svg width="12" height="12"><use href="#mark"/></svg></span></div>
    <div class="card-img" role="img" aria-label="Salon scene with long wavy auburn hair" style="left:218px;top:727px;background:linear-gradient(150deg,#6e5a50,#2d2a2c 50%,#b0673a)"><span class="bm"><svg width="12" height="12"><use href="#mark"/></svg></span></div>

    <p class="ctitle" style="left:34px;top:924px">Best Organic Beauty Products</p>
    <p class="ctitle" style="left:218px;top:924px">Ultimate Spa Day Essentials</p>
    <div class="count" style="left:34px;top:973px"><span class="avs"><i></i><i></i><i></i></span><p class="num">432<span>Members</span></p></div>
    <div class="count" style="left:218px;top:973px"><span class="avs"><i></i><i></i><i></i></span><p class="num">123<span>Members</span></p></div>
    <div class="soft-btn" style="left:34px;top:1023px;width:165px">Invite</div>
    <div class="solid-btn" style="left:218px;top:1023px;width:165px">Join</div>

    <div class="scroll" style="top:1088px"></div>
    <nav class="nav" style="top:1123px">
      <span class="it"><svg width="22" height="22"><use href="#home"/></svg></span>
      <span class="it"><svg width="22" height="22"><use href="#store"/></svg></span>
      <span class="on"><span class="it" style="background:var(--grad)"><svg width="20" height="20"><use href="#globe"/></svg></span>DISCOVER</span>
      <span class="it"><svg width="22" height="22"><use href="#chat"/></svg></span>
    </nav>
  </section>

</main>
</body>
</html>
```